New Business and Accounting Software need a Web Site

The website is for a Business and Accounting Software that has 8 products.
Each product has its owns logo and color, when you do the design have in consideration that we are looking the experience that when you change from one product page to another the look and feel adjust to the color and logo of the product.
The product are:
Ventas (Sales)
Compras (Purchases)
Contabilidad (Accounting)
Presupuesto (Budget)
Inventarios (Inventory)
Bancos (Banks)
NĂ³mina RH (Human Resources Payroll)
CRM (Customer Relationship Manager)

You can see how the main logo and variations are used in each page
- https://www.ufta.com/
- https://www.vemi.com/
- https://www.prulvin.com/

Our goal is to be similar to them.

I have created a word document to explain what I want.
You need to design:
1 Home Page
1 Product Landing Page
1 Product Detail Page
1 Price Page

I am attaching:
1. Main Logo
2. 8 Product Logos
3. Website Idea, you can create your own idea.

You are welcome to use other icons for the each product if you want.

Target Market(s)

Independet professionals and Small and Medium Companies

Industry/Entity Type

Business and Accounting Software

Coding

Coded - Design and coding required

Colors
0054AA
0677BA
7BADD7
CADEEF
E8F1F8

Requirements
Must have
• Must show all products in the main page

```html
<!DOCTYPE html>
<html lang="en">
<head>
<meta charset="utf-8">
<title>nubra.co — Business and Accounting Software</title>
<link href="https://fonts.googleapis.com/css2?family=Poppins:wght@400;500;600;700;800&display=swap" rel="stylesheet">
<style>
:root{
  --blue:#0054AA;--blue-mid:#0677BA;--blue-soft:#7BADD7;--blue-pale:#CADEEF;--blue-mist:#E8F1F8;
  --ink:#1d2433;--text:#555c66;--line:#c9ced6;--white:#fff;
  --ventas:#e8862a;--compras:#3f8fd2;--contab:#b0439f;--presu:#1f9b7a;
  --inv:#c0333e;--bancos:#4e4e4e;--nomina:#3fae9e;--crm:#4b4db8;
}
*{box-sizing:border-box;margin:0;padding:0}
html,body{width:1200px;height:3972px;overflow:hidden;background:var(--white);font-family:'Poppins',sans-serif;color:var(--ink)}
.page{position:relative;width:1200px;height:3972px;overflow:hidden}
.abs{position:absolute}
.bg{position:absolute;left:0;top:0}

/* header */
.site-header{position:absolute;left:0;top:0;width:1200px;height:90px;border-bottom:1px solid #e3e7ec;background:var(--white);z-index:5}
.brand{position:absolute;left:145px;top:18px;display:flex;align-items:center;gap:10px;color:var(--blue);font-weight:700;font-size:40px;line-height:1}
.brand .dot{width:46px;height:46px;border-radius:50%;background:var(--blue)}
.nav{position:absolute;top:30px;left:398px;display:flex;gap:0;font-size:14px;font-weight:500}
.nav a{position:absolute;white-space:nowrap;color:var(--ink);text-decoration:none}
.nav a.active{color:var(--blue-mid)}
.nav-underline{position:absolute;left:398px;top:86px;width:64px;height:4px;background:var(--blue-mid)}
.lang{position:absolute;left:782px;top:33px;display:flex;align-items:center;gap:8px}
.lang .flag{width:22px;height:14px;background:var(--blue);border:1px solid #c33}
.caret{width:0;height:0;border-left:6px solid transparent;border-right:6px solid transparent;border-top:7px solid var(--ink)}

.btn{position:absolute;display:flex;align-items:center;justify-content:center;gap:10px;border-radius:30px;color:var(--white);font-weight:700;font-size:12px;letter-spacing:.3px;white-space:nowrap}
.btn svg{width:18px;height:12px}
.btn-dark{background:var(--blue)}
.btn-light{background:var(--blue-soft)}

/* hero */
.hero-title{position:absolute;left:143px;top:158px;font-weight:800;font-size:53px;line-height:56px;color:var(--blue)}
.hero-title .soft{color:var(--blue-soft)}
.hero-text{position:absolute;left:143px;top:348px;width:340px;font-size:14.5px;line-height:24px;color:var(--text)}
.slider-dots{position:absolute;left:365px;top:570px;display:flex;gap:12px}
.slider-dots span{width:9px;height:9px;border-radius:50%;background:#c5cad2}
.slider-dots span.on{background:var(--blue-mid)}
.slide-num{position:absolute;left:362px;top:640px;font-weight:700;font-size:14px;color:var(--blue)}
.slide-bar{position:absolute;left:389px;top:588px;width:3px;height:78px;background:var(--blue)}

/* section headings */
.sec-head{position:absolute;left:0;width:1200px;text-align:center}
.ghost{position:absolute;left:0;width:1200px;text-align:center;font-weight:800;font-size:88px;color:#eceef1;letter-spacing:2px;line-height:1}
.sec-title{position:absolute;left:0;width:1200px;text-align:center;font-weight:700;font-size:48px;color:var(--blue);line-height:1}
.sec-title .soft{color:var(--blue-soft)}
.sec-dot{position:absolute;width:20px;height:20px;border-radius:50%;background:var(--blue-soft)}

/* products */
.card{position:absolute;width:449px;height:233px;background:var(--white);box-shadow:0 6px 18px rgba(20,40,80,.08);display:flex}
.card .art{width:197px;height:100%}
.card .info{flex:1;padding:24px 18px 0 34px;position:relative}
.card.outlined .info{outline:2px solid #f0b26b;outline-offset:-2px}
.plogo{display:flex;align-items:center;gap:8px}
.plogo .pdot{width:36px;height:36px;border-radius:50%;background:var(--blue)}
.plogo .pname{font-weight:700;font-size:34px;line-height:1;color:var(--blue)}
.plabel{font-size:10px;letter-spacing:4px;margin:2px 0 0 44px;font-weight:500;text-transform:uppercase}
.pdesc{margin-top:18px;font-size:12.5px;line-height:19.5px;color:var(--text)}
.more{position:absolute;left:34px;top:190px;font-weight:700;font-size:13px;text-decoration:underline}

/* screen */
.screen{position:absolute;left:296px;top:1991px;width:611px;height:307px;background:#1b2333;border-radius:10px;padding:10px 10px 12px}
.screen .inner{width:100%;height:100%;background:var(--white);position:relative;overflow:hidden}

/* about */
.about-title{position:absolute;left:146px;top:2357px;font-weight:700;font-size:48px;color:var(--white);line-height:1}
.about-ghost{position:absolute;left:170px;top:2378px;font-weight:800;font-size:82px;color:rgba(255,255,255,.08);line-height:1}
.about-sub{position:absolute;left:145px;top:2478px;font-weight:700;font-size:22px;color:var(--white)}
.about-text{position:absolute;left:146px;top:2530px;width:411px;font-size:13.2px;line-height:22.4px;color:var(--white);text-align:justify}
.photo{position:absolute;left:620px;top:2373px;width:564px;height:564px;border-radius:50%;background:linear-gradient(135deg,#6d7f93 0%,#c9d3dd 45%,#f1f3f5 75%,#8d96a0 100%)}

/* contact */
.field{position:absolute;border:1px solid var(--line);background:var(--white);font-size:12px;color:#555;padding:0 24px;display:flex;align-items:center}
.field.msg{align-items:flex-start;padding-top:14px}

/* footer */
.footer-brand{position:absolute;left:535px;top:3650px;display:flex;align-items:center;gap:18px;color:var(--blue);font-weight:700;font-size:84px;line-height:1}
.footer-brand .dot{width:104px;height:104px;border-radius:50%;background:var(--blue)}
.fnav{position:absolute;left:177px;top:3850px;font-size:14px;font-weight:500;color:var(--ink);white-space:nowrap}
.fnav span{margin:0 12px}
.copy{position:absolute;left:177px;top:3885px;font-size:11px;color:var(--text)}
.social{position:absolute;top:3923px;width:24px;height:24px;border-radius:50%;background:var(--blue)}
.news-head{position:absolute;left:629px;top:3845px;font-weight:700;font-size:18px;color:var(--ink)}
.news-input{position:absolute;left:629px;top:3890px;width:310px;height:38px;border:1px solid var(--line);border-radius:20px;font-size:11px;color:#555;padding-left:26px;display:flex;align-items:center}
</style>
</head>
<body>
<div class="page">

<!-- hero background -->
<svg class="bg" width="1200" height="800" viewBox="0 0 1200 800">
  <ellipse cx="160" cy="270" rx="430" ry="230" fill="var(--blue-mist)"/>
  <circle cx="1140" cy="330" r="120" fill="none" stroke="var(--blue-mist)" stroke-width="50"/>
  <polygon points="0,398 375,735 1200,398 1200,412 378,755 0,420" fill="var(--blue-soft)"/>
  <circle cx="766" cy="324" r="232" fill="var(--blue)"/>
</svg>

<header class="site-header">
  <div class="brand"><span class="dot"></span>nubra.co</div>
  <nav class="nav">
    <a class="active" style="left:0">● Home</a>
    <a style="left:88px">Soluciones</a>
    <a style="left:196px">Prices</a>
    <a style="left:267px">Contact Us</a>
  </nav>
  <div class="lang"><span class="flag"></span><span class="caret"></span></div>
  <div class="btn btn-dark" style="left:848px;top:22px;width:90px;height:34px;font-size:10px">SIGN IN <svg viewBox="0 0 18 12"><path d="M1 6h15M11 1l5 5-5 5" stroke="#fff" stroke-width="1.6" fill="none"/></svg></div>
  <div class="btn btn-light" style="left:948px;top:22px;width:106px;height:34px;font-size:10px">FREE TRIAL <svg viewBox="0 0 18 12"><path d="M1 6h15M11 1l5 5-5 5" stroke="#fff" stroke-width="1.6" fill="none"/></svg></div>
  <div class="nav-underline"></div>
</header>

<h1 class="hero-title">Business and<br><span class="soft">Accounting</span><br>Software</h1>
<p class="hero-text">Sed ut perspiciatis unde omnis iste natus error sit voluptatem accusantium</p>
<div class="btn btn-dark" style="left:143px;top:428px;width:145px;height:38px">FREE TRIAL <svg viewBox="0 0 18 12"><path d="M1 6h15M11 1l5 5-5 5" stroke="#fff" stroke-width="1.6" fill="none"/></svg></div>
<div class="btn btn-light" style="left:296px;top:428px;width:145px;height:38px">LEARN MORE <svg viewBox="0 0 18 12"><path d="M1 6h15M11 1l5 5-5 5" stroke="#fff" stroke-width="1.6" fill="none"/></svg></div>
<div class="slider-dots"><span></span><span class="on"></span><span></span><span></span></div>
<div class="slide-bar"></div>
<div class="slide-num">02</div>

<div class="abs" role="img" aria-label="Desktop monitor showing the accounting dashboard" style="left:540px;top:170px;width:480px;height:580px;border-radius:24px;background:linear-gradient(160deg,#ffffff 0%,#eef1f5 60%,#d6dbe2 100%);transform:rotate(-14deg) skewX(-6deg);box-shadow:0 20px 40px rgba(0,30,70,.18)"></div>

<!-- products -->
<div class="ghost" style="top:812px">PRODUCTS</div>
<div class="sec-title" style="top:802px">Our <span class="soft">Products</span></div>
<div class="sec-dot" style="left:590px;top:862px"></div>

<svg class="bg" width="1200" height="3972" viewBox="0 0 1200 3972" style="pointer-events:none">
  <path d="M143 1011H71V2020H293" fill="none" stroke="#9aa3ad" stroke-width="1.5" stroke-dasharray="6 6"/>
</svg>

<div class="card outlined" style="left:146px;top:925px">
  <div class="art" role="img" aria-label="Sales icon: handshake and coin" style="background:linear-gradient(160deg,#f4b15a,#e0701c)"></div>
  <div class="info">
    <div class="plogo"><span class="pdot"></span><span class="pname">nubra</span></div>
    <div class="plabel" style="color:var(--ventas)">Ventas</div>
    <p class="pdesc">Lorem ipsum dolor sit amet, consectetur adipiscing elit, sed do eiusmod tempor incididunt ut labore et dolore magna</p>
    <a class="more" style="color:var(--ventas)">READ MORE</a>
  </div>
</div>
<div class="card" style="left:604px;top:925px">
  <div class="art" role="img" aria-label="Purchases icon: shopping cart with tick" style="background:linear-gradient(160deg,#8cbde6,#2f7dc4)"></div>
  <div class="info">
    <div class="plogo"><span class="pdot"></span><span class="pname">nubra</span></div>
    <div class="plabel" style="color:var(--compras)">Compras</div>
    <p class="pdesc">Lorem ipsum dolor sit amet, consectetur adipiscing elit, sed do eiusmod tempor incididunt ut labore et dolore magna</p>
    <a class="more" style="color:var(--compras)">READ MORE</a>
  </div>
</div>

<div class="card" style="left:146px;top:1166px">
  <div class="info">
    <div class="plogo"><span class="pdot"></span><span class="pname">nubra</span></div>
    <div class="plabel" style="color:var(--contab)">Contabilidad</div>
    <p class="pdesc">Lorem ipsum dolor sit amet, consectetur adipiscing elit, sed do eiusmod tempor incididunt ut labore et dolore magna</p>
    <a class="more" style="color:var(--contab)">READ MORE</a>
  </div>
  <div class="art" role="img" aria-label="Accounting icon: receipt and calculator" style="background:linear-gradient(160deg,#e28fd0,#a13594)"></div>
</div>
<div class="card" style="left:604px;top:1166px">
  <div class="info">
    <div class="plogo"><span class="pdot"></span><span class="pname">nubra</span></div>
    <div class="plabel" style="color:var(--presu)">Presupuesto</div>
    <p class="pdesc">Lorem ipsum dolor sit amet, consectetur adipiscing elit, sed do eiusmod tempor incididunt ut labore et dolore magna</p>
    <a class="more" style="color:var(--presu)">READ MORE</a>
  </div>
  <div class="art" role="img" aria-label="Budget icon: money bag and calculator" style="background:linear-gradient(160deg,#4fcdb5,#12806a)"></div>
</div>

<div class="card" style="left:146px;top:1406px">
  <div class="art" role="img" aria-label="Inventory icon: boxes with gear" style="background:linear-gradient(160deg,#e07a80,#b1222d)"></div>
  <div class="info">
    <div class="plogo"><span class="pdot"></span><span class="pname">nubra</span></div>
    <div class="plabel" style="color:var(--inv)">Inventarios</div>
    <p class="pdesc">Lorem ipsum dolor sit amet, consectetur adipiscing elit, sed do eiusmod tempor incididunt ut labore et dolore magna</p>
    <a class="more" style="color:var(--inv)">READ MORE</a>
  </div>
</div>
<div class="card" style="left:604px;top:1406px">
  <div class="art" role="img" aria-label="Banks icon: bank building" style="background:linear-gradient(160deg,#8a8a8a,#3a3a3a)"></div>
  <div class="info">
    <div class="plogo"><span class="pdot"></span><span class="pname">nubra</span></div>
    <div class="plabel" style="color:var(--bancos)">Bancos</div>
    <p class="pdesc">Lorem ipsum dolor sit amet, consectetur adipiscing elit, sed do eiusmod tempor incididunt ut labore et dolore magna</p>
    <a class="more" style="color:var(--bancos)">READ MORE</a>
  </div>
</div>

<div class="card" style="left:146px;top:1647px">
  <div class="info">
    <div class="plogo"><span class="pdot"></span><span class="pname">nubra</span></div>
    <div class="plabel" style="color:var(--nomina)">Nómina RH</div>
    <p class="pdesc">Lorem ipsum dolor sit amet, consectetur adipiscing elit, sed do eiusmod tempor incididunt ut labore et dolore magna</p>
    <a class="more" style="color:var(--nomina)">READ MORE</a>
  </div>
  <div class="art" role="img" aria-label="Payroll icon: employee with coins" style="background:linear-gradient(160deg,#8fdccd,#2f9e8c)"></div>
</div>
<div class="card" style="left:604px;top:1647px">
  <div class="info">
    <div class="plogo"><span class="pdot"></span><span class="pname">nubra</span></div>
    <div class="plabel" style="color:var(--crm)">CRM</div>
    <p class="pdesc">Lorem ipsum dolor sit amet, consectetur adipiscing elit, sed do eiusmod tempor incididunt ut labore et dolore magna</p>
    <a class="more" style="color:var(--crm)">READ MORE</a>
  </div>
  <div class="art" role="img" aria-label="CRM icon: connected customers" style="background:linear-gradient(160deg,#8a8ee0,#3b3aa8)"></div>
</div>

<!-- about background -->
<svg class="bg" style="top:2050px" width="1200" height="1000" viewBox="0 2050 1200 1000">
  <path d="M0 2415 Q600 1850 1200 2415 L1200 2770 L372 3015 L0 2820 Z" fill="var(--blue)"/>
  <polygon points="0,2835 372,3035 1200,2790 1200,2806 372,3056 0,2858" fill="var(--blue-soft)"/>
</svg>

<div class="screen" role="img" aria-label="Laptop screen showing the suppliers list of the app">
  <div class="inner">
    <div style="height:14px;background:var(--blue)"></div>
    <div style="margin:22px 14px 0;height:8px;background:#e6e9ee"></div>
    <div style="margin:8px 14px 0;height:1px;background:#d3d8df"></div>
    <div style="margin:12px 14px 0;height:1px;background:#e3e6eb"></div>
    <div style="margin:12px 14px 0;height:1px;background:#e3e6eb"></div>
    <div style="position:absolute;left:0;right:0;bottom:0;height:10px;background:var(--blue)"></div>
  </div>
</div>
<div class="sec-dot" style="left:286px;top:2012px;background:var(--white);border:4px solid var(--blue-mid)"></div>

<div class="about-ghost">ABOUT</div>
<h2 class="about-title">About Us</h2>
<div class="sec-dot" style="left:146px;top:2423px;background:var(--blue-pale)"></div>
<h3 class="about-sub">SED UT PERSPICIATIS UNDE OMNIS</h3>
<p class="about-text">Lorem ipsum dolor sit amet, consectetur adipiscing elit, sed do eiusmod tempor incididunt ut labore et dolore magna aliqua. Quis ipsum suspendisse ultrices gravida. Risus commodo viverra maecenas accumsan lacus vel facilisis. Lorem ipsum dolor sit amet, consectetur adipiscing elit, sed do eiusmod tempor incididunt ut labore et dolore magna aliqua. Quis ipsum suspendisse ultrices gravida. Risus commodo viverra maecenas accumsan lacus vel facilisis. Lorem ipsum dolor sit amet, consectetur adipiscing elit, sed do eiusmod tempor incididunt ut labore et dolore</p>
<div class="btn btn-dark" style="left:146px;top:2773px;width:145px;height:40px;background:var(--blue-mid)">FREE TRIAL <svg viewBox="0 0 18 12"><path d="M1 6h15M11 1l5 5-5 5" stroke="#fff" stroke-width="1.6" fill="none"/></svg></div>
<div class="btn btn-light" style="left:299px;top:2773px;width:145px;height:40px">LEARN MORE <svg viewBox="0 0 18 12"><path d="M1 6h15M11 1l5 5-5 5" stroke="#fff" stroke-width="1.6" fill="none"/></svg></div>
<div class="photo" role="img" aria-label="Photo of hands working on a laptop and calculator over financial charts"></div>

<!-- contact -->
<div class="ghost" style="top:3108px">CONTACT</div>
<div class="sec-title" style="top:3108px">Contact <span class="soft">Us</span></div>
<div class="sec-dot" style="left:590px;top:3168px"></div>
<div class="field" style="left:185px;top:3247px;width:403px;height:40px">NAME</div>
<div class="field" style="left:185px;top:3303px;width:403px;height:40px">E MAIL</div>
<div class="field" style="left:185px;top:3359px;width:403px;height:40px">PHONE</div>
<div class="field msg" style="left:612px;top:3247px;width:403px;height:153px">MESSAGE</div>
<div class="btn btn-dark" style="left:527px;top:3447px;width:145px;height:40px">SUBMIT <svg viewBox="0 0 18 12"><path d="M1 6h15M11 1l5 5-5 5" stroke="#fff" stroke-width="1.6" fill="none"/></svg></div>

<!-- footer -->
<svg class="bg" style="top:3500px" width="1200" height="472" viewBox="0 3500 1200 472">
  <path d="M0 3972 L0 3790 L410 3560 L820 3600 L1200 3500 L1200 3972 Z" fill="var(--blue-mist)"/>
  <polygon points="0,3830 560,3540 1200,3820 1200,3834 560,3556 0,3848" fill="var(--blue-pale)"/>
  <line x1="170" y1="3800" x2="1030" y2="3800" stroke="#d7dde5"/>
</svg>
<div class="footer-brand"><span class="dot"></span>nubra.co</div>
<div class="fnav">HOME<span>/</span>SOLUCIONES<span>/</span>PRICES<span>/</span>CONTACT US</div>
<div class="copy">Copyrights @ 2022 nubra.co All Rights Reserved | Privacy | Terms of Use</div>
<div class="social" style="left:179px;background:#1da1f2"></div>
<div class="social" style="left:216px"></div>
<div class="social" style="left:253px;background:#0a3a78"></div>
<div class="news-head">SIGN UP NEWSLETTER</div>
<div class="news-input">Enter Email</div>
<div class="btn btn-dark" style="left:922px;top:3890px;width:100px;height:38px;background:var(--blue-mid)">SIGN UP <svg viewBox="0 0 18 12"><path d="M1 6h15M11 1l5 5-5 5" stroke="#fff" stroke-width="1.6" fill="none"/></svg></div>

</div>
</body>
</html>
```